Hemp company needs website/online store

We are a startup hemp company and we need an online storefront designed. We are very open do design, but will include our logo to help. We make 100% hemp derived products like edibles, concentrates, vapes and THCA flower. Everything is grown locally, and all products are extracted and made in house.

Requirements
Nice to have
• I would like to highlight that we have Cannabis products that are hemp derived and 100% legal across the US. Also that all cannabis is locally grown and products are extracted and made in house and sent out for third party lab testing.

```html
<!DOCTYPE html>
<html lang="en">
<head>
<meta charset="utf-8">
<title>Meadowline Hemp</title>
<link href="https://fonts.googleapis.com/css2?family=Poppins:wght@400;500;600;700&display=swap" rel="stylesheet">
<style>
:root{
  --green-deep:#2f6a22;
  --green:#3f7d2b;
  --green-mid:#4e8c35;
  --lime:#8fb83c;
  --lime-bright:#a6c93a;
  --pale:#f1f8ec;
  --white:#ffffff;
  --text:#4a4a4a;
  --star:#f0a81c;
}
*{margin:0;padding:0;box-sizing:border-box}
html,body{width:1200px;height:5259px;overflow:hidden}
body{font-family:'Poppins',sans-serif;color:var(--text);position:relative;background:var(--white)}
.abs{position:absolute}
.center{text-align:center}
a{color:inherit;text-decoration:none}

/* hero */
.hero{top:0;left:0;width:1200px;height:895px;background:radial-gradient(ellipse at 50% 60%,#4d7a36 0%,#2c4f22 55%,#1a3314 100%)}
.nav-band{top:0;left:0;width:1200px;height:160px;background:rgba(20,40,15,.35)}
.brand{font-weight:600;color:var(--white);font-size:34px;line-height:1;white-space:nowrap}
.brand-mark{width:40px;height:40px;border-radius:50%;background:var(--lime);display:inline-block;vertical-align:middle;margin-right:12px}
.nav{top:70px;left:575px;display:flex;gap:34px;font-size:13px;color:var(--white)}
.nav .active{color:var(--lime-bright);border-bottom:2px solid var(--lime-bright);padding-bottom:16px}
.hero-title{top:310px;left:0;width:1200px;color:var(--white);font-size:62px;line-height:62px;font-weight:600;letter-spacing:1px}
.hero-sub{top:371px;left:0;width:1200px;color:var(--white);font-size:40px;line-height:51px;font-weight:400}
.hero-text{top:482px;left:0;width:1200px;color:var(--white);font-size:20px;line-height:36px}
.btn-outline{top:600px;left:425px;width:350px;height:92px;border:2px solid var(--white);color:var(--white);font-size:21px;display:flex;align-items:center;justify-content:center;font-weight:500}

/* headings */
.sec-mark{width:44px;height:44px;border-radius:50%;background:var(--lime)}
.sec-title{font-size:56px;font-weight:600;color:var(--green);line-height:1;white-space:nowrap}
.sec-sub{font-size:17px;font-weight:500;color:var(--lime)}

/* products */
.tile{overflow:hidden}
.tile-label{left:0;bottom:0;width:100%;height:98px;background:rgba(143,184,60,.85);color:var(--white);font-size:24px;font-weight:500;display:flex;align-items:center;justify-content:center}
.tile-edibles{top:1180px;left:88px;width:626px;height:380px;background:linear-gradient(135deg,#5b9440,#4a8532);color:var(--white)}
.tile-edibles h3{font-size:27px;font-weight:500;margin-top:88px}
.tile-edibles p{font-size:15px;line-height:26px;margin:24px auto 0;width:440px}
.btn-small{display:inline-block;margin-top:24px;background:var(--lime-bright);color:var(--white);font-size:13px;padding:9px 26px}

/* why */
.why{top:2078px;left:0;width:1200px;height:630px;background:linear-gradient(180deg,#3f7b2c,#3a7328)}
.feat{top:2362px;width:260px;color:var(--white)}
.feat-ring{width:146px;height:146px;border-radius:50%;background:var(--lime);margin:0 auto;display:flex;align-items:center;justify-content:center}
.feat-ring .inner{width:118px;height:118px;border-radius:50%;background:var(--white);display:flex;align-items:center;justify-content:center}
.feat h4{font-size:19px;font-weight:600;margin-top:30px}
.feat p{font-size:15px;line-height:24px;margin-top:10px;font-weight:400}

/* about */
.about{top:2708px;left:0;width:1200px;height:617px;background:var(--pale)}
.about-block{top:2830px;left:95px;width:400px;height:380px;border:22px solid var(--green);display:flex;align-items:center;justify-content:center;font-size:34px;font-weight:600;color:var(--green)}
.about-text{top:2927px;left:585px;width:516px;font-size:15px;line-height:31px}
.btn-solid{background:var(--green);color:var(--white);display:flex;align-items:center;justify-content:center;font-weight:500}

/* quote */
.quote{top:3325px;left:0;width:1200px;height:628px;background:linear-gradient(90deg,#1f3d18 0%,#3b6d2a 35%,#4a8632 60%,#4a8632 100%)}
.quote-kicker{top:3452px;left:520px;color:var(--white);font-size:24px}
.quote-head{top:3500px;left:520px;color:var(--white);font-size:56px;font-weight:600;line-height:72px}
.quote-head span{color:var(--lime-bright)}

/* testimonials */
.card{top:4245px;width:330px;height:315px;background:var(--white);border-radius:30px;box-shadow:0 6px 26px rgba(0,0,0,.12)}
.avatar{top:-40px;left:30px;width:72px;height:72px;border-radius:50%;background:linear-gradient(#c9b8a6,#8c7a68);border:4px solid var(--white)}
.qmark{top:18px;right:34px;font-size:110px;line-height:1;color:#dfe9cf;font-weight:700}
.card p{position:absolute;top:70px;left:40px;width:250px;font-size:15px;line-height:23px;text-align:justify;color:#3c3c3c}
.card .line{top:200px;left:40px;width:250px;height:1px;background:#e3e3e3}
.card .who{top:218px;left:40px;font-size:13px;font-weight:600;color:var(--green)}
.card .role{top:236px;left:40px;font-size:10px;color:var(--lime)}
.card .stars{top:216px;right:40px;color:var(--star);font-size:12px;letter-spacing:1px}

/* footer */
.footer{top:4705px;left:0;width:1200px;height:495px;background:linear-gradient(180deg,#3f7b2c,#356d24)}
.news{top:4768px;left:147px;width:901px;height:125px;background:var(--lime)}
.news h3{position:absolute;top:38px;left:36px;font-size:34px;font-weight:600;color:var(--white)}
.news .field{position:absolute;top:40px;left:465px;width:400px;height:46px;border-radius:23px;background:var(--white);font-size:11px;color:#777;padding:15px 28px}
.news .go{position:absolute;top:40px;left:745px;width:120px;height:46px;border-radius:23px;background:var(--green);color:var(--white);font-size:15px;display:flex;align-items:center;justify-content:center;font-weight:500}
.foot-brand{top:4965px;left:185px;width:260px;text-align:center;color:var(--white);font-weight:600;font-size:26px;line-height:1;white-space:nowrap}
.foot-brand .brand-mark{display:block;margin:0 auto 14px;width:44px;height:44px}
.foot-h{font-size:16px;font-weight:500;color:var(--white)}
.foot-list{list-style:none;font-size:15px;color:var(--white);line-height:30px}
.foot-list li::before{content:"›";margin-right:16px}
.contact-row{display:flex;gap:22px;align-items:center;color:var(--white);font-size:14px;line-height:18px}
.c-icon{width:30px;height:30px;border:1px solid var(--white);border-radius:4px;display:flex;align-items:center;justify-content:center;flex:none}
.social{top:5110px;left:239px;display:flex;gap:8px}
.social span{width:32px;height:32px;border:2px solid var(--white);border-radius:4px;display:block}
.bottom{top:5200px;left:0;width:1200px;height:59px;background:var(--lime);color:var(--white);font-size:13px}
</style>
</head>
<body>

<!-- hero -->
<section class="abs hero" role="img" aria-label="Close-up photo of hemp leaves"></section>
<div class="abs nav-band"></div>
<div class="abs brand" style="top:75px;left:85px"><span class="brand-mark"></span>Meadowline Hemp</div>
<nav class="abs nav">
  <a class="active">HOME</a><a>ABOUT US</a><a>PRODUCTS ▾</a><a>SHOP</a><a>BLOG</a><a>CONTACT US</a>
</nav>
<h1 class="abs hero-title center">CANNABIS PRODUCTS</h1>
<p class="abs hero-sub center">that are hemp derived and 100%<br>legal across the US.</p>
<p class="abs hero-text center">All cannabis is locally grown and products are extracted and<br>made in house and sent out for third party lab testing.</p>
<a class="abs btn-outline">VIEW OUR PRODUCTS</a>

<!-- products -->
<div class="abs sec-mark" style="top:980px;left:578px"></div>
<h2 class="abs sec-title" style="top:1040px;left:410px">Our Products</h2>
<p class="abs sec-sub" style="top:1102px;left:593px">WHAT WE PROVIDE</p>

<div class="abs tile tile-edibles center">
  <h3>EDIBLES</h3>
  <p>Lorem ipsum dolor sit amet, consectetur adipiscing elit, sed do eiusmod tempor incididunt ut labore et dolore magna aliqua. Quis ipsum suspendisse</p>
  <span class="btn-small">READ MORE</span>
</div>
<div class="abs tile" style="top:1180px;left:729px;width:383px;height:380px;background:linear-gradient(160deg,#b9b36a,#6f8a3a 60%,#3f5e24)" role="img" aria-label="Photo of a hemp concentrate bud">
  <div class="abs tile-label">CONCENTRATES</div>
</div>
<div class="abs tile" style="top:1577px;left:88px;width:383px;height:380px;background:linear-gradient(160deg,#b8a285,#7a6a52 55%,#56713a)" role="img" aria-label="Photo of a dropper bottle with hemp leaf">
  <div class="abs tile-label">VAPES</div>
</div>
<div class="abs tile" style="top:1577px;left:487px;width:625px;height:380px;background:linear-gradient(170deg,#e8ebe2,#8aa36a 45%,#5d7d3e)" role="img" aria-label="Photo of dried hemp flower buds">
  <div class="abs tile-label">THCA FLOWER</div>
</div>

<!-- why -->
<section class="abs why" role="img" aria-label="Hemp leaf background in green"></section>
<div class="abs sec-mark" style="top:2168px;left:578px;background:var(--white)"></div>
<h2 class="abs sec-title" style="top:2235px;left:376px;color:var(--white)">Why Choose Us</h2>
<p class="abs sec-sub" style="top:2298px;left:711px;color:var(--lime-bright)">WHY HEMP</p>

<div class="abs feat center" style="left:70px">
  <div class="feat-ring"><div class="inner">
    <svg width="60" height="60" viewBox="0 0 60 60" fill="none" stroke="#3f7d2b" stroke-width="2"><path d="M30 50V20M30 40L14 30M30 40L46 30M30 32L20 14M30 32L40 14"/></svg>
  </div></div>
  <h4>ORGANIC CANNABIS</h4>
  <p>Lorem ipsum dolor sit amet,<br>con sectetur adipiscing elit.</p>
</div>
<div class="abs feat center" style="left:332px">
  <div class="feat-ring"><div class="inner">
    <svg width="60" height="60" viewBox="0 0 60 60" fill="none" stroke="#3f7d2b" stroke-width="2"><rect x="18" y="20" width="24" height="30" rx="3"/><rect x="23" y="10" width="14" height="10"/><path d="M30 28v14M23 35h14"/></svg>
  </div></div>
  <h4>ALSO FOR MEDICAL</h4>
  <p>Lorem ipsum dolor sit amet,<br>con sectetur adipiscing elit.</p>
</div>
<div class="abs feat center" style="left:600px">
  <div class="feat-ring"><div class="inner">
    <svg width="60" height="60" viewBox="0 0 60 60" fill="none" stroke="#3f7d2b" stroke-width="2"><circle cx="30" cy="30" r="20"/><path d="M10 30h40M30 10c-8 8-8 32 0 40M30 10c8 8 8 32 0 40"/></svg>
  </div></div>
  <h4>DELIVERY SERVICE 24/7</h4>
  <p>Lorem ipsum dolor sit amet,<br>con sectetur adipiscing elit.</p>
</div>
<div class="abs feat center" style="left:868px">
  <div class="feat-ring"><div class="inner">
    <svg width="60" height="60" viewBox="0 0 60 60" fill="none" stroke="#3f7d2b" stroke-width="2"><circle cx="30" cy="22" r="10"/><path d="M25 22l4 4 6-7M10 40l10 8h16M50 40l-10 8"/></svg>
  </div></div>
  <h4>BEST PERFORMANCE</h4>
  <p>Lorem ipsum dolor sit amet,<br>con sectetur adipiscing elit.</p>
</div>

<!-- about -->
<section class="abs about"></section>
<div class="abs about-block">Meadowline</div>
<div class="abs sec-mark" style="top:2798px;left:821px"></div>
<h2 class="abs sec-title" style="top:2850px;left:746px;font-size:40px">About Us</h2>
<p class="abs sec-sub" style="top:2893px;left:838px;font-size:13px">WHO WE ARE</p>
<p class="abs about-text center">Lorem ipsum dolor sit amet, consectetur adipiscing elit, sed do eiusmod tempor incididunt ut labore et dolore magna aliqua. Ut enim ad minim veniam, quis nostrud exercitation ullamco laboris nisi ut aliquip ex ea commodo consequat. Duis aute irure dolor in reprehenderit in voluptate velit esse cillum dolore eu fugiat nulla pariatur. Excepteur sint occaecat cupidatat non proident, sunt in culpa qui officia .</p>
<a class="abs btn-solid" style="top:3183px;left:763px;width:160px;height:52px;font-size:13px">KNOW MORE</a>

<!-- quote -->
<section class="abs quote" role="img" aria-label="Hemp plant photo fading into green"></section>
<p class="abs quote-kicker">GET A QUOTE</p>
<h2 class="abs quote-head">We Are Here For Your<br>Estimate <span>CANABIS</span><br>Product Price</h2>
<a class="abs btn-solid" style="top:3733px;left:523px;width:250px;height:76px;font-size:25px;background:var(--lime-bright)">CALL NOW</a>

<!-- testimonials -->
<div class="abs sec-mark" style="top:4035px;left:578px"></div>
<h2 class="abs sec-title" style="top:4100px;left:354px">Our Testimonials</h2>
<p class="abs sec-sub" style="top:4160px;left:681px">CLIENT REVIEWS</p>

<div class="abs card" style="left:75px">
  <div class="abs avatar" role="img" aria-label="Client portrait"></div>
  <div class="abs qmark">“</div>
  <p>Lorem ipsum dolor sit amet, conse ctetuer adipiscing elit. Aenean comodo ligula eget dolor. Aenean massa. Cum sociis</p>
  <div class="abs line"></div>
  <div class="abs who">Marcus Hale</div><div class="abs role">Managing Director</div>
  <div class="abs stars">★★★★★</div>
</div>
<div class="abs card" style="left:433px">
  <div class="abs avatar" role="img" aria-label="Client portrait"></div>
  <div class="abs qmark">“</div>
  <p>Lorem ipsum dolor sit amet, conse ctetuer adipiscing elit. Aenean comodo ligula eget dolor. Aenean massa. Cum sociis</p>
  <div class="abs line"></div>
  <div class="abs who">Priya Rowan</div><div class="abs role">Managing Director</div>
  <div class="abs stars">★★★★★</div>
</div>
<div class="abs card" style="left:791px">
  <div class="abs avatar" role="img" aria-label="Client portrait"></div>
  <div class="abs qmark">“</div>
  <p>Lorem ipsum dolor sit amet, conse ctetuer adipiscing elit. Aenean comodo ligula eget dolor. Aenean massa. Cum sociis</p>
  <div class="abs line"></div>
  <div class="abs who">Elliot Vance</div><div class="abs role">Managing Director</div>
  <div class="abs stars">★★★★★</div>
</div>
<a class="abs btn-solid" style="top:4551px;left:486px;width:228px;height:60px;font-size:19px">VIEW MORE</a>

<!-- footer -->
<footer class="abs footer" role="img" aria-label="Green hemp leaf background"></footer>
<div class="abs news">
  <h3>Our Newsletter Sign Up</h3>
  <div class="field">Enter Email Address</div>
  <div class="go">SIGNUP</div>
</div>
<div class="abs foot-brand"><span class="brand-mark"></span>Meadowline Hemp</div>
<div class="abs social"><span></span><span></span><span></span><span></span></div>

<div class="abs" style="top:4942px;left:495px">
  <p class="foot-h">Quik Links</p>
  <ul class="foot-list" style="margin-top:14px">
    <li>Home</li><li>About Us</li><li>Products</li><li>Blog</li><li>Contact Us</li>
  </ul>
</div>
<div class="abs" style="top:4942px;left:712px">
  <p class="foot-h">Contact Details</p>
  <div class="contact-row" style="margin-top:24px">
    <div class="c-icon"><svg width="14" height="14" viewBox="0 0 14 14" fill="#fff"><path d="M3 1l2 3-1 1.5c1 2 2.5 3.5 4.5 4.5L10 9l3 2-1 2C6 13 1 8 1 2z"/></svg></div>
    <div>CALL US<br>555 014 2298</div>
  </div>
  <div class="contact-row" style="margin-top:24px">
    <div class="c-icon"><svg width="14" height="12" viewBox="0 0 14 12" fill="none" stroke="#fff" stroke-width="1.4"><rect x="1" y="1" width="12" height="10"/><path d="M1 1l6 5 6-5"/></svg></div>
    <div>EMAIL US<br>hello@meadowlinehemp.com</div>
  </div>
  <div class="contact-row" style="margin-top:22px">
    <div class="c-icon"><svg width="12" height="16" viewBox="0 0 12 16" fill="#fff"><path d="M6 0a6 6 0 0 1 6 6c0 4-6 10-6 10S0 10 0 6a6 6 0 0 1 6-6zm0 3.5a2.5 2.5 0 1 0 0 5 2.5 2.5 0 0 0 0-5z"/></svg></div>
    <div>Address line here dummy<br>Address line here</div>
  </div>
</div>

<div class="abs bottom">
  <span class="abs" style="top:21px;left:86px">Copyright ©2023 - All Rights Reserved by Company name</span>
  <span class="abs" style="top:16px;left:680px;display:flex;align-items:center;gap:10px">
    <svg width="26" height="24" viewBox="0 0 26 24"><path d="M13 1l12 22H1z" fill="#fff"/><path d="M13 8v8M13 18v2" stroke="#8fb83c" stroke-width="2.4"/></svg>
    Disclaimer that products may cause you to fail a drug test
  </span>
</div>

</body>
</html>
```